DL Flyer and magnet design

I am in need of a new flyer design to show some offers on each side. First side Water filtration. Second side Heat pump hot water. I will attach an existing design from a previous flyer/magnet. I have also got some information to go on the flyer and images/logo.

Side 1: Water Filtration Solutions
Coral Ridge Pipeworks and Heating
Fresh, Clean Water for Every Tap

Water Filtration Solutions
1️⃣ High Flow Water Filtration
Starting from just $550!

2️⃣ Whole House Water Filtration
Enjoy pure water throughout your home – starting from $1800!

3️⃣ Whole House Water Filtration with UV Lamp (Perfect for rainwater systems)
Get the ultimate filtration – starting from $3000!

🎁 FREE BRAVO COOLER
With every water filtration system or referral!

📞 Call us today: 0491 837 254
🌐 Visit our website: www.coralridgeph.example.au

💧 Better water, better life. Call now for a free quote!

Side 2: Heat Pump Hot Water Systems
Energy-Efficient Hot Water Solutions

Heat Pump Hot Water Systems
🌟 Rebates Available!
Save big with government incentives on energy-efficient hot water systems.

💼 All Major Makes, Models, and Sizes
We supply and install trusted brands to suit your household’s needs.

💳 Interest-Free Finance Options
Upgrade now and pay later with flexible payment plans.

🎁 FREE BRAVO COOLER
With every heat pump system or referral!

💧 Upgrade to energy-efficient hot water and save!

Please include on the flyer. Valid until 30/6/2-25 Images are for illustrative purposes only and may not represent the exact product or service provided

```html
<!DOCTYPE html>
<html lang="en">
<head>
<meta charset="utf-8">
<title>Coral Ridge Pipeworks and Heating – DL Flyer</title>
<link href="https://fonts.googleapis.com/css2?family=Archivo+Narrow:ital,wght@0,400;0,500;0,600;0,700;1,700&family=Roboto+Condensed:wght@500;600;700&display=swap" rel="stylesheet">
<style>
  :root {
    --bg: #8a8a8a;
    --paper: #ffffff;
    --ink: #111111;
    --blue: #2b3590;
    --orange: #f47b20;
    --shadow: rgba(0,0,0,0.35);
  }
  * { margin: 0; padding: 0; box-sizing: border-box; }
  html, body { width: 1200px; height: 1200px; overflow: hidden; background: var(--bg); }
  body { position: relative; font-family: "Archivo Narrow", "Arial Narrow", sans-serif; color: var(--ink); }

  .flyer {
    position: absolute; top: 71px; width: 498px; height: 1055px;
    background: var(--paper); box-shadow: 0 4px 14px var(--shadow); overflow: hidden;
  }
  .flyer--filtration { left: 82px; }
  .flyer--heatpump { left: 620px; }
  .abs { position: absolute; }

  .brand { display: flex; align-items: center; gap: 14px; color: var(--blue); font-weight: 700; }
  .brand__mark { width: 56px; height: 56px; background: var(--blue); flex: none; }
  .brand__name { font-size: 29px; line-height: 1.05; }

  .headline { font-family: "Roboto Condensed", "Arial Narrow", sans-serif; font-weight: 600; line-height: 1; }
  .headline--dark { color: var(--ink); }
  .headline--orange { color: var(--orange); }

  .offer { left: 30px; width: 320px; font-size: 18px; line-height: 1.4; }
  .offer__title { font-weight: 700; text-transform: uppercase; font-size: 18.5px; }

  .price-tag {
    left: 356px; width: 142px; height: 53px; background: var(--blue); color: var(--orange);
    font-family: "Roboto Condensed", sans-serif; font-weight: 700; font-size: 31px;
    display: flex; align-items: center; justify-content: center;
    box-shadow: 0 10px 8px -4px var(--shadow);
  }

  .gift { font-family: "Archivo Narrow", sans-serif; font-style: italic; font-weight: 700; font-size: 39px; line-height: 1; }
  .gift--orange { color: var(--orange); }
  .gift--blue { color: var(--blue); }
  .gift-note { font-size: 18px; }

  .contact { left: 0; width: 100%; text-align: center; font-size: 18px; }
  .contact__phone { font-family: "Roboto Condensed", sans-serif; font-style: italic; font-weight: 700; font-size: 37px; }
  .contact__phone--blue { color: var(--blue); }
  .contact__phone--orange { color: var(--orange); }

  .band { left: 0; width: 100%; display: flex; align-items: center; justify-content: center; color: #fff; font-size: 19px; }
  .band--blue { background: var(--blue); top: 979px; height: 76px; }
  .band--orange { background: var(--orange); top: 784px; height: 76px; }

  .intro { left: 32px; font-weight: 700; font-size: 18.5px; line-height: 1.35; text-transform: uppercase; }
  .feature { left: 32px; width: 440px; font-size: 18px; line-height: 1.4; }
  .feature__title { color: var(--orange); font-weight: 700; text-transform: uppercase; font-size: 19px; }
  .validity { left: 42px; top: 1001px; font-size: 18px; }
</style>
</head>
<body>

<section class="flyer flyer--filtration">
  <div class="brand abs" style="left:30px; top:140px;">
    <span class="brand__mark"></span>
    <span class="brand__name">CORAL RIDGE<br>Pipeworks and Heating</span>
  </div>

  <h1 class="headline headline--dark abs" style="left:30px; top:219px; font-size:50px;">WATER FILTRATION</h1>
  <h2 class="headline headline--orange abs" style="left:28px; top:262px; font-size:80px;">SOLUTIONS</h2>

  <div class="offer abs" style="top:392px;">
    <div class="offer__title">High Flow Water Filtration</div>
    <div>Starting from just</div>
  </div>
  <div class="price-tag abs" style="top:388px;">$550!</div>

  <div class="offer abs" style="top:494px;">
    <div class="offer__title">Whole House Water Filtration</div>
    <div>Enjoy pure water throughout your home – starting from</div>
  </div>
  <div class="price-tag abs" style="top:488px;">$1800!</div>

  <div class="offer abs" style="top:622px;">
    <div class="offer__title">Whole House Water Filtration<br>with UV Lamp</div>
    <div>(Perfect for rainwater systems)<br>Get the ultimate filtration – starting from</div>
  </div>
  <div class="price-tag abs" style="top:614px;">$3000!</div>

  <div class="gift gift--orange abs" style="left:30px; top:784px;">FREE BRAVO COOLER</div>
  <div class="gift-note abs" style="left:30px; top:826px;">With every water filtration system or referral!</div>

  <div class="contact abs" style="top:878px;">Call us today: <span class="contact__phone contact__phone--blue">0491 837 254</span></div>
  <div class="contact abs" style="top:928px;">Visit our website: www.coralridgeph.example.au</div>

  <div class="band band--blue abs">Better water, better life. Call now for a free quote!</div>
</section>

<section class="flyer flyer--heatpump">
  <h1 class="headline headline--orange abs" style="left:40px; top:40px; font-size:86px;">HEAT PUMP</h1>
  <h2 class="headline headline--dark abs" style="left:42px; top:124px; font-size:45px;">HOT WATER SYSTEMS</h2>

  <p class="intro abs" style="top:212px;">Coral Ridge Pipeworks and Heating<br>Energy-efficient hot water solutions</p>

  <div class="feature abs" style="top:306px;">
    <div class="feature__title">Rebates Available!</div>
    <div>Save big with government incentives on energy-efficient hot water systems.</div>
  </div>
  <div class="feature abs" style="top:408px;">
    <div class="feature__title">All Major Makes, Models, and Sizes</div>
    <div>We supply and install trusted brands to suit your household’s needs.</div>
  </div>
  <div class="feature abs" style="top:510px;">
    <div class="feature__title">Interest-Free Finance Options</div>
    <div>Upgrade now and pay later with flexible payment plans.</div>
  </div>

  <div class="gift gift--blue abs" style="left:32px; top:590px;">FREE BRAVO COOLER</div>
  <div class="gift-note abs" style="left:32px; top:632px;">With every heat pump system or referral!</div>

  <div class="contact abs" style="top:684px;">Call us today: <span class="contact__phone contact__phone--orange">0491 837 254</span></div>
  <div class="contact abs" style="top:734px;">Visit our website: www.coralridgeph.example.au</div>

  <div class="band band--orange abs">Upgrade to energy-efficient hot water and save!</div>

  <div class="brand abs" style="left:42px; top:892px;">
    <span class="brand__mark"></span>
    <span class="brand__name">CORAL RIDGE<br>Pipeworks and Heating</span>
  </div>

  <div class="validity abs">*Valid until 30-06-2025</div>
</section>

</body>
</html>
```